Business Card Design EFTPOS Comparison site

At QuoteLark.com.au we are a free service that allows our customers to get up to five quotes from our panel of suppliers for a range of BUSINESS related products and services. These products include eftpos / credit card machines, bank accounts, insurance, signage,office furniture etc. basically anything that a small business would need.
The process is done in 3 steps; 1) register your enquiry 2) we source and provide the five cheapest quotes 3) then select the supplier of your choice,the process is simple QuoteLark and is FREE.
Please visit the soon to be revamped website to see our logo.
Target Market(s)
Small business operators
Industry/Entity Type
Small Business
Requirements
Must have
- Double Sided card

```html
<!DOCTYPE html>
<html lang="en">
<head>
<meta charset="utf-8">
<title>QuoteLark.com.au Business Card</title>
<link rel="stylesheet" href="https://fonts.googleapis.com/css2?family=Quicksand:wght@400;500;600;700&display=swap">
<style>
  :root {
    --backdrop: #e9e7e4;
    --card: #ffffff;
    --orange: #f08a1c;
    --orange-deep: #e9731a;
    --ink-grey: #6f6f6f;
    --line-grey: #9a9a9a;
    --shadow: rgba(0, 0, 0, 0.18);
  }
  * { box-sizing: border-box; margin: 0; padding: 0; }
  html, body {
    width: 1200px;
    height: 1000px;
    overflow: hidden;
    background: var(--backdrop);
    font-family: "Quicksand", sans-serif;
  }
  .sheet {
    position: relative;
    width: 1200px;
    height: 1000px;
  }
  .card {
    position: absolute;
    left: 290px;
    width: 620px;
    height: 340px;
    background: var(--card);
    box-shadow: 0 6px 22px var(--shadow);
    overflow: hidden;
  }
  .card--front { top: 100px; }
  .card--back { top: 540px; }

  .wordmark {
    display: flex;
    align-items: center;
    gap: 12px;
    color: var(--orange);
    font-weight: 700;
  }
  .wordmark__dot {
    border-radius: 50%;
    background: var(--orange);
    flex: none;
  }
  .card--front .wordmark {
    position: absolute;
    left: 0;
    right: 0;
    top: 135px;
    justify-content: center;
    font-size: 46px;
  }
  .card--front .wordmark__dot { width: 34px; height: 34px; }

  .card--back .wordmark {
    position: absolute;
    right: 34px;
    top: 48px;
    font-size: 28px;
    gap: 8px;
  }
  .card--back .wordmark__dot { width: 20px; height: 20px; }

  .contact {
    position: absolute;
    left: 82px;
    top: 140px;
  }
  .contact__name {
    font-size: 30px;
    font-weight: 500;
    color: var(--orange);
    letter-spacing: 0.5px;
    line-height: 1;
  }
  .contact__role {
    margin-top: 6px;
    font-size: 13px;
    font-weight: 500;
    letter-spacing: 1.2px;
    text-transform: uppercase;
    color: var(--ink-grey);
    padding-bottom: 6px;
    border-bottom: 1.5px solid var(--orange);
    width: 172px;
  }
  .contact__lines {
    margin-top: 18px;
    font-size: 11.5px;
    font-weight: 500;
    color: var(--ink-grey);
    line-height: 17px;
    list-style: none;
  }
  .contact__label {
    color: var(--orange-deep);
    font-weight: 700;
  }
</style>
</head>
<body>
  <main class="sheet">
    <section class="card card--front" aria-label="Card front">
      <div class="wordmark">
        <span class="wordmark__dot" aria-hidden="true"></span>
        <span class="wordmark__name">QuoteLark.com.au</span>
      </div>
    </section>

    <section class="card card--back" aria-label="Card back">
      <div class="wordmark">
        <span class="wordmark__dot" aria-hidden="true"></span>
        <span class="wordmark__name">QuoteLark.com.au</span>
      </div>
      <div class="contact">
        <h1 class="contact__name">Nora Pell</h1>
        <p class="contact__role">Executive Director</p>
        <ul class="contact__lines">
          <li>4417 Harbor Lane Brookvale, NSW 2100</li>
          <li><span class="contact__label">t:</span> 555 210 734</li>
          <li><span class="contact__label">e:</span> hello@quotelark.com.au</li>
        </ul>
      </div>
    </section>
  </main>
</body>
</html>
```